New Business Card for Auto Repair and Performance Shop!

Need a redesign on a card that we have used for a while now. Something more update and modern, Serious but not too serious. Something confident, that shows the client that we are bespoke. Adding value.

Target Market(s)

Foreign Auto Repair and Performance

Industry/Entity Type

Automotive

Contact Information for Business Card

Utilize Logo, would like to change car silhouette to something Veltra,

Font styles to use
Sans Serif

Requirements
Must have
• business name, address, website, phone number.
MotoSerenix
4918 W. Birchwell Rd
Brackenfield, T.X. 76990
1-254-487-3106
www.moto-serenix-example.com

Specializing in Asian, European, and Domestic Auto Repair, Performance and Fabrication.

Clear space on back to for space to write appointment time and which client advisor helped the client.
Nice to have
• Up to the designers,

```html
<!DOCTYPE html>
<html lang="en">
<head>
<meta charset="utf-8">
<title>MotoSerenix Business Card</title>
<link href="https://fonts.googleapis.com/css2?family=Barlow:wght@500;600;700&display=swap" rel="stylesheet">
<style>
  :root {
    --backdrop: #b8d8e2;
    --navy: #0d0d56;
    --ink: #1f1d66;
    --paper: #ffffff;
  }
  html, body {
    margin: 0;
    padding: 0;
    width: 1071px;
    height: 1200px;
    overflow: hidden;
    background: var(--backdrop);
    font-family: "Barlow", "DIN Alternate", sans-serif;
  }
  .canvas {
    position: relative;
    width: 1071px;
    height: 1200px;
  }
  .card {
    position: absolute;
    left: 61px;
    width: 950px;
    height: 488px;
    background: var(--paper);
    overflow: hidden;
  }
  .card--front { top: 81px; }
  .card--back { top: 630px; }

  .front-panel {
    position: absolute;
    inset: 0;
    width: 100%;
    height: 100%;
  }
  .front-edge {
    position: absolute;
    top: 0;
    right: 0;
    width: 13px;
    height: 100%;
    background: var(--navy);
  }
  .brand-mark {
    position: absolute;
    display: flex;
    align-items: center;
    justify-content: center;
    gap: 12px;
    font-weight: 700;
    white-space: nowrap;
  }
  .brand-mark__dot {
    display: inline-block;
    border-radius: 50%;
  }
  .brand-mark--front {
    left: 40px;
    top: 80px;
    width: 390px;
    font-size: 46px;
    color: var(--paper);
  }
  .brand-mark--front .brand-mark__dot {
    width: 20px;
    height: 20px;
    background: var(--paper);
  }
  .tagline {
    position: absolute;
    left: 30px;
    width: 410px;
    top: 272px;
    margin: 0;
    color: var(--paper);
    font-weight: 500;
    font-size: 28px;
    line-height: 36.5px;
    text-align: center;
  }
  .contact {
    position: absolute;
    left: 470px;
    width: 470px;
    top: 0;
    height: 100%;
    color: var(--navy);
    text-align: center;
  }
  .contact__name {
    position: absolute;
    left: 0; right: 0;
    top: 70px;
    margin: 0;
    font-size: 46px;
    font-weight: 700;
    line-height: 1;
  }
  .contact__address {
    position: absolute;
    left: 0; right: 0;
    top: 197px;
    margin: 0;
    font-style: normal;
    font-size: 28px;
    font-weight: 500;
    line-height: 37px;
  }
  .contact__phone,
  .contact__web {
    position: absolute;
    left: 0; right: 0;
    margin: 0;
    font-size: 28px;
    font-weight: 500;
    line-height: 1;
  }
  .contact__phone { top: 315px; }
  .contact__web { top: 390px; font-size: 26px; color: var(--ink); }

  .brand-mark--back {
    left: 0;
    width: 100%;
    top: 128px;
    font-size: 96px;
    color: var(--navy);
    gap: 20px;
  }
  .brand-mark--back .brand-mark__dot {
    width: 36px;
    height: 36px;
    background: var(--navy);
  }
  .appointment {
    position: absolute;
    left: 162px;
    width: 627px;
    top: 368px;
    height: 36px;
    border-bottom: 3px solid var(--ink);
    color: var(--ink);
    font-size: 28px;
    font-weight: 500;
  }
  .appointment__label {
    position: absolute;
    bottom: 0;
    line-height: 1;
  }
  .appointment__label--date { left: 2px; }
  .appointment__label--time { left: 370px; }
</style>
</head>
<body>
<main class="canvas">
  <section class="card card--front" aria-label="Business card front">
    <svg class="front-panel" viewBox="0 0 950 488" preserveAspectRatio="none" aria-hidden="true">
      <polygon points="0,0 439,0 512,488 0,488" fill="var(--navy)"/>
    </svg>
    <div class="front-edge"></div>

    <div class="brand-mark brand-mark--front">
      <span class="brand-mark__dot"></span>
      <span class="brand-mark__name">MotoSerenix</span>
    </div>

    <p class="tagline">Specializing in Asian,<br>European, and Domestic<br>Auto Repair, Performance<br>and Fabrication.</p>

    <div class="contact">
      <h1 class="contact__name">MotoSerenix</h1>
      <address class="contact__address">4918 W. Birchwell Rd<br>Brackenfield, T.X. 76990</address>
      <p class="contact__phone">1-254-487-3106</p>
      <p class="contact__web">www.moto-serenix-example.com</p>
    </div>
  </section>

  <section class="card card--back" aria-label="Business card back">
    <div class="brand-mark brand-mark--back">
      <span class="brand-mark__dot"></span>
      <span class="brand-mark__name">MotoSerenix</span>
    </div>

    <div class="appointment">
      <span class="appointment__label appointment__label--date">Date</span>
      <span class="appointment__label appointment__label--time">Time</span>
    </div>
  </section>
</main>
</body>
</html>
```